KIVO 248
I need double sided standard sized Business Card [3.5" x 2"]
Open to designers choice
Modern
Pavel Rudakovsky
PO BOX 7132
Lorvale, OR 90318
pavel@tumq4.com
kivo248.com

```html
<!DOCTYPE html>
<html lang="en">
<head>
<meta charset="utf-8">
<title>KIVO 248 — Business Card</title>
<link href="https://fonts.googleapis.com/css2?family=Michroma&display=swap" rel="stylesheet">
<style>
  :root {
    --page-bg: #e9e6e2;
    --card-white: #ffffff;
    --orange-light: #f7762f;
    --orange-mid: #ee4e1c;
    --orange-deep: #d9361a;
    --curve-shadow: #3a1d14;
    --ink-light: #ffffff;
    --brand-orange: #ef5a1e;
  }
  * { margin: 0; padding: 0; box-sizing: border-box; }
  html, body {
    width: 1200px; height: 914px; overflow: hidden;
    background: var(--page-bg);
    font-family: "Michroma", sans-serif;
  }
  .business-card {
    position: absolute; left: 100px; top: 171px;
    width: 1000px; height: 572px;
    background: var(--card-white);
    box-shadow: 0 10px 30px rgba(0,0,0,0.18);
    overflow: hidden;
  }
  .card-background { position: absolute; inset: 0; width: 100%; height: 100%; }
  .holder-name {
    position: absolute; left: 58px; top: 42px;
    color: var(--ink-light); font-size: 20px; letter-spacing: 2px;
    white-space: nowrap;
  }
  .holder-title {
    position: absolute; left: 58px; top: 72px;
    color: var(--ink-light); font-size: 16px; letter-spacing: 2px;
  }
  .contact-list {
    position: absolute; left: 58px; top: 262px;
    list-style: none; color: var(--ink-light);
    font-size: 14px; letter-spacing: 1.5px;
    white-space: nowrap;
  }
  .contact-item { display: flex; align-items: center; height: 31px; }
  .contact-icon {
    width: 20px; height: 20px; border-radius: 50%;
    background: var(--ink-light); margin-right: 16px;
    display: flex; align-items: center; justify-content: center;
    flex-shrink: 0;
  }
  .contact-icon svg { width: 12px; height: 12px; }
  .contact-icon.is-blank { background: transparent; }
  .brand-mark {
    position: absolute; left: 620px; top: 230px; width: 330px;
    display: flex; flex-direction: column; align-items: center; gap: 26px;
  }
  .brand-square {
    width: 90px; height: 90px; background: var(--brand-orange);
  }
  .brand-name {
    color: var(--brand-orange); font-size: 36px; letter-spacing: 2px;
    white-space: nowrap;
  }
</style>
</head>
<body>
  <div class="business-card">
    <svg class="card-background" viewBox="0 0 1000 572" preserveAspectRatio="none" aria-hidden="true">
      <defs>
        <radialGradient id="orangeField" cx="0.45" cy="0.3" r="0.8">
          <stop offset="0" stop-color="#f7762f"/>
          <stop offset="0.6" stop-color="#ee4e1c"/>
          <stop offset="1" stop-color="#d9361a"/>
        </radialGradient>
      </defs>
      <path d="M0 0 H610 C470 90 560 200 520 300 C480 400 440 470 455 572 H0 Z" fill="#3a1d14" opacity="0.85"/>
      <path d="M0 0 H595 C455 90 545 200 505 300 C465 400 425 470 440 572 H0 Z" fill="url(#orangeField)"/>
    </svg>

    <div class="holder-name">Pavel Rudakovsky</div>
    <div class="holder-title">CEO</div>

    <ul class="contact-list">
      <li class="contact-item">
        <span class="contact-icon"><svg viewBox="0 0 12 12"><path d="M6 1a3.5 3.5 0 0 0-3.5 3.5C2.5 7.5 6 11 6 11s3.5-3.5 3.5-6.5A3.5 3.5 0 0 0 6 1z" fill="#ee4e1c"/><circle cx="6" cy="4.5" r="1.2" fill="#fff"/></svg></span>
        PO BOX 7132
      </li>
      <li class="contact-item"><span class="contact-icon is-blank"></span>Lorvale, OR 90318</li>
      <li class="contact-item">
        <span class="contact-icon"><svg viewBox="0 0 12 12"><path d="M3 1.5l1.6 2.4-1 1a6 6 0 0 0 3.5 3.5l1-1 2.4 1.6-.8 1.5C5.5 10.5 1.5 6.5 1.5 2.3z" fill="#ee4e1c"/></svg></span>
        5553026140
      </li>
      <li class="contact-item">
        <span class="contact-icon"><svg viewBox="0 0 12 12"><rect x="2" y="3" width="8" height="6" rx="1" fill="#ee4e1c"/></svg></span>
        5558712093
      </li>
      <li class="contact-item">
        <span class="contact-icon"><svg viewBox="0 0 12 12"><rect x="3.5" y="1.5" width="5" height="9" rx="1" fill="#ee4e1c"/></svg></span>
        5553026140
      </li>
      <li class="contact-item">
        <span class="contact-icon"><svg viewBox="0 0 12 12"><rect x="1.5" y="3" width="9" height="6" fill="#ee4e1c"/><path d="M1.5 3l4.5 3.5L10.5 3" stroke="#fff" fill="none"/></svg></span>
        pavel@tumq4.com
      </li>
      <li class="contact-item">
        <span class="contact-icon"><svg viewBox="0 0 12 12"><circle cx="6" cy="6" r="4.2" stroke="#ee4e1c" stroke-width="1.3" fill="none"/><path d="M1.8 6h8.4M6 1.8c-2 2.5-2 5.9 0 8.4M6 1.8c2 2.5 2 5.9 0 8.4" stroke="#ee4e1c" fill="none"/></svg></span>
        www.kivo248.com
      </li>
    </ul>

    <div class="brand-mark">
      <span class="brand-square"></span>
      <span class="brand-name">KIVO 248</span>
    </div>
  </div>
</body>
</html>
```